Real Estate Brochure/ door flyer.

I am looking for a brochure that can be put in a plastic door hanger bag and distributed as I walk throughout neighborhoods. It should be mainly directed towards Sellers, but have a nod to Buyers as well since once sold, the person will need to buy.
I was planning on a tri fold brochure, but am open to other styles. I do have a bio, and am on the fence as to whether or not to include it.

Target Market(s)

Owners of residential homes and potential buyers of the same

Industry/Entity Type

Real Estate

Colors

Designer to choose colors to be used in the design.

Requirements
Must have
• The service promises I have made, our logo,
• My contact information, email and cell phone.
• I'm looking for something bright and clean looking.
• There is an equal housing opportunity symbol and Vendarix symbol that is required by law, I am trying to find artwork for it. As well as "Not intended to solicit represented parties" has to be on the brochure somewhere.
Nice to have
• Photos of homeowner's in a nice home. I like mixed family relationships. Interracial, same sex couples and young couples just starting out.
Should not have
• Any form of deadline or timeline to respond.

```html
<!DOCTYPE html>
<html lang="en">
<head>
<meta charset="utf-8">
<title>Halvorsen Real Estate – About Dale Corrigan</title>
<link rel="stylesheet" href="https://fonts.googleapis.com/css2?family=Source+Sans+3:wght@400;600;700&family=Roboto+Slab:wght@700&display=swap">
<style>
  :root {
    --brand-red: #e8232d;
    --paper: #ffffff;
    --ink-white: #ffffff;
    --logo-ink: #8e1b20;
    --glow: #bfeef6;
    --photo-light: #d6e3ea;
    --photo-deep: #b7ada1;
  }
  * { box-sizing: border-box; margin: 0; padding: 0; }
  html, body { width: 1200px; height: 933px; overflow: hidden; background: var(--paper); }
  body { font-family: "Source Sans 3", "Myriad Pro", Arial, sans-serif; }

  .brochure-panel { position: relative; width: 1200px; height: 933px; background: var(--paper); }

  .red-field { position: absolute; left: 0; top: 0; }

  .agent-portrait { position: absolute; left: 42px; top: 46px; width: 336px; height: 326px; }

  .bio {
    position: absolute; left: 27px; top: 396px; width: 365px;
    color: var(--ink-white); font-size: 20.5px; line-height: 29.5px; text-align: justify;
  }
  .bio p { text-indent: 52px; margin-bottom: 29.5px; }

  .causes {
    position: absolute; left: 416px; top: 18px; width: 362px; color: var(--ink-white);
  }
  .cause { margin-bottom: 28px; }
  .cause h2 {
    font-size: 22px; font-weight: 700; line-height: 29px; text-align: center;
    letter-spacing: 0.2px; margin-bottom: 1px; hyphens: auto; -webkit-hyphens: auto;
  }
  .cause p {
    font-size: 20.5px; line-height: 29.5px; text-align: justify; text-indent: 52px;
    hyphens: auto; -webkit-hyphens: auto;
  }

  .contact {
    position: absolute; left: 402px; top: 702px; width: 386px; text-align: center; color: var(--brand-red);
  }
  .contact-label {
    display: inline-block; width: 232px; height: 41px; border-radius: 21px; background: var(--brand-red);
    color: var(--ink-white); font-family: "Roboto Slab", Rockwell, Georgia, serif; font-weight: 700;
    font-size: 21px; line-height: 41px;
  }
  .contact-lines { margin-top: 14px; font-size: 27px; line-height: 35px; }
  .site-address {
    position: absolute; left: 402px; top: 897px; width: 386px; text-align: center;
    color: var(--brand-red); font-size: 20px; letter-spacing: 0.4px;
  }

  .family-photo {
    position: absolute; left: 802px; top: 0; width: 398px; height: 933px;
    background: linear-gradient(180deg, var(--photo-light) 0%, var(--photo-deep) 100%);
  }

  .logo-badge { position: absolute; left: 858px; top: 100px; width: 294px; height: 282px; }
  .logo-name {
    position: absolute; left: 858px; top: 218px; width: 294px; text-align: center;
    color: var(--logo-ink); font-weight: 700; font-size: 30px; line-height: 32px; letter-spacing: 2px;
  }
  .logo-name span { display: block; font-size: 19px; letter-spacing: 5px; }
</style>
</head>
<body>
<main class="brochure-panel">
  <svg class="red-field" width="802" height="933" viewBox="0 0 802 933" aria-hidden="true">
    <path fill="var(--brand-red)" d="M37 15 H765 Q788 15 788 38 V664 Q788 687 765 687 H402 V908 Q402 930 380 930 H37 Q15 930 15 908 V37 Q15 15 37 15 Z"/>
  </svg>

  <svg class="agent-portrait" viewBox="0 0 336 326" role="img" aria-label="Portrait photo of agent Dale Corrigan">
    <defs>
      <linearGradient id="portraitTone" x1="0" y1="0" x2="0" y2="1">
        <stop offset="0" stop-color="#8a6a55"/>
        <stop offset="1" stop-color="#d9c6b8"/>
      </linearGradient>
    </defs>
    <path d="M96 6 H240 Q256 6 264 20 L326 150 Q332 163 326 176 L264 306 Q256 320 240 320 H96 Q80 320 72 306 L10 176 Q4 163 10 150 L72 20 Q80 6 96 6 Z" fill="var(--paper)"/>
    <path d="M101 16 H235 Q249 16 256 28 L314 152 Q319 163 314 174 L256 298 Q249 310 235 310 H101 Q87 310 80 298 L22 174 Q17 163 22 152 L80 28 Q87 16 101 16 Z" fill="url(#portraitTone)"/>
  </svg>

  <section class="bio">
    <p>Since 1983, I have been buying and selling realestate, specializing in income producing multi-family properties as well as single family rehab/flip type properties.</p>
    <p>I became a Vendarix in 2007, where I have been able to use my experiences in real estate investing to help contractors as well as first time home buyers to realize their home ownership and investment goals.</p>
    <p>Keeping in line with “helping others”, I feel it a moral obligation to help those less fortunate among us; to “give back” as the saying goes. I work with and support the following organizations:</p>
  </section>

  <section class="causes">
    <article class="cause">
      <h2>Connecticut Alliance of Shared Care Homes (CASCH)</h2>
      <p>I am the Treasurer of this organization which provides 1,600 beds, in one hundred homes across the State of Connecticut providing housing to mentally and physically disabled people of our communities.</p>
    </article>
    <article class="cause">
      <h2>Alas de Salud</h2>
      <p>I serve as a board member and the trip coordinator for the International Chapter that organizes medical and dental relief missions in Guatemala.</p>
    </article>
    <article class="cause">
      <h2>Second Wing Rescue Flights</h2>
      <p>I am the President and pilot for this not-for-profit organization which provides free transportation of animals from shelters facing euthanasia to rescues and adoption centers, where they will find new homes.</p>
    </article>
  </section>

  <section class="contact">
    <div class="contact-label">Contact Me</div>
    <div class="contact-lines">
      <div>Dale Corrigan</div>
      <div>dale.homes@harborline.net</div>
      <div>860-555-0147</div>
    </div>
  </section>
  <div class="site-address">HALVORSENREALESTATE.COM</div>

  <div class="family-photo" role="img" aria-label="Photo of a smiling family standing in front of their home"></div>

  <svg class="logo-badge" viewBox="0 0 294 282" aria-hidden="true">
    <path d="M82 8 H212 Q230 8 239 24 L284 124 Q291 141 284 158 L239 258 Q230 274 212 274 H82 Q64 274 55 258 L10 158 Q3 141 10 124 L55 24 Q64 8 82 8 Z" fill="var(--paper)" stroke="var(--glow)" stroke-width="8"/>
  </svg>
  <div class="logo-name">HALVORSEN<span>REAL ESTATE</span></div>
</main>
</body>
</html>
```